| 希望する色 | 特になし・その他 追記事項: 周囲の景色に埋没しないような色合いを希望します。 |
戸建賃貸住宅6棟の計画「ミドリテラス・カサネル」の看板デザインの依頼です。 【 概要 】 全6棟の戸建賃貸住宅を建築中です。 建築地が住宅街の中にあり場所がわかりにくいため、大通りから見える場所へ看板を掲出したいと考えています。 周辺にある戸建賃貸住宅は規格モノを建てただけですが、地元工務店と組んで自然環境を重視した計画としました。 賃貸住宅でも環境重視の方、都市部から郊外へ引っ越しをしてくる方、などにアピールしたいと思っています。 シンプルかつデザイン性の高い看板デザインを募集します。 【 依頼内容 】 ・看板サイズ:横3,000mm × 縦2,000mm ・看板の素材:メッシュターポリン(予定) ・デザイン素材:計画名のロゴは用意したものを使用してください。他はお任せします。 ・デザイン内容:「戸建賃貸住宅」は明示してください。建築地案内は矢印程度で良いかと考えています。敷地レイアウトの明示は不要です。 ・デザインの利用について:看板への使用が主目的ですが、HPへの掲載、不動産仲介業者への配布等も行う場合があります。作成デザインを尊重し編集、合成、切り抜き等は原則行いません。他制限事項あればお知らせください。 【 契約金額(税抜) 】 70,000円(税別) ※契約金額(税込)からシステム利用料を差し引いた金額が、ワーカーさまの受取金額となります その他ご質問等ありましたら、気軽にお問い合わせください。 ご応募をお待ちしております! |
| https://fuyoreside.sitelume.jp | ||
シンプルでもバランスが良く看板の目的に合致したデザインでした。
沢山のご提案ありがとうございました。良い案が幾つもあり採用デザインを1つに絞るのは悩みました。また機会がありましたらよろしくお願いします。

```html
<!DOCTYPE html>
<html lang="ja">
<head>
<meta charset="utf-8">
<title>ミドリテラス・カサネル 戸建賃貸住宅 入居者募集</title>
<link rel="stylesheet" href="https://fonts.googleapis.com/css2?family=Noto+Sans+JP:wght@300;900&display=swap">
<style>
  :root {
    --sky: #17a9de;
    --teal: #12a3a6;
    --meadow: #1d9a55;
    --paper: #ffffff;
    --ink: #231f20;
    --accent: #e4561c;
    --arrow-label: #1a8fc4;
  }
  html, body {
    margin: 0;
    padding: 0;
    overflow: hidden;
    background: #ffffff;
  }
  .signboard {
    position: relative;
    width: 1200px;
    height: 800px;
    overflow: hidden;
    background: linear-gradient(180deg, var(--sky) 0%, var(--teal) 45%, var(--meadow) 100%);
    font-family: "Noto Sans JP", sans-serif;
  }
  .route-arrow {
    position: absolute;
    left: 0;
    top: 0;
  }
  .headline {
    position: absolute;
    left: 80px;
    margin: 0;
    font-weight: 900;
    white-space: nowrap;
    line-height: 1;
  }
  .headline--lead {
    top: 158px;
    font-size: 72px;
    color: var(--accent);
    letter-spacing: 1px;
  }
  .headline--main {
    top: 262px;
    font-size: 118px;
    color: var(--ink);
    letter-spacing: 2px;
  }
  .direction-label {
    position: absolute;
    left: 982px;
    top: 182px;
    margin: 0;
    font-size: 40px;
    font-weight: 900;
    color: var(--arrow-label);
    line-height: 1;
  }
  .recruit {
    position: absolute;
    right: 142px;
    top: 452px;
    margin: 0;
    font-size: 48px;
    font-weight: 900;
    color: var(--accent);
    line-height: 1;
    letter-spacing: 2px;
  }
  .project-name {
    position: absolute;
    left: 0;
    width: 1200px;
    top: 594px;
    margin: 0;
    text-align: center;
    font-size: 64px;
    font-weight: 300;
    color: var(--paper);
    letter-spacing: 6px;
    line-height: 1;
  }
</style>
</head>
<body>
  <main class="signboard">
    <svg class="route-arrow" width="1200" height="800" viewBox="0 0 1200 800" aria-hidden="true">
      <path fill="#ffffff" fill-rule="evenodd"
        d="M76 130 H1082 V100 L1160 176 L1090 248 V530 H76 Z
           M940 232 H1040 V430 H940 Z"/>
    </svg>

    <h1 class="headline headline--lead">自然環境を重視した</h1>
    <p class="headline headline--main">戸建賃貸住宅</p>
    <p class="direction-label">こちら</p>
    <p class="recruit">入居者募集</p>
    <p class="project-name">ミドリテラス・カサネル</p>
  </main>
</body>
</html>
```